Wedding Decor and Entertianment business card

Company - We run a weddings and events company called Amber Finch, we provide most entertainment and decor services to our customers.

Initial idea is ....
A simple business card with logo on the front, this will be spot varnish. On a matt black background.
The reverse will be simple contact information.

But happy to try things outside of the box and would welcome some crazy ideas.

Target Market(s)

wedding couples - 21 - 40
High end wedding venues.

Industry/Entity Type

Wedding

Contact Information for Business Card

01492 718 263
amberfinchevents.co.uk
rowan@amberfinchevents.co.uk
or
helena@amberfinchevents.co.uk

Requirements
Nice to have
• black matt background with spot varnish logo on the front.

```html
<!DOCTYPE html>
<html lang="en">
<head>
<meta charset="utf-8">
<title>Amber Finch – Business Card</title>
<link rel="stylesheet" href="https://fonts.googleapis.com/css2?family=Jost:wght@400;500&display=swap">
<style>
  :root {
    --backdrop: #3b3b3d;
    --card-black: #141414;
    --card-white: #ffffff;
    --ink: #2b2b2b;
    --plum: #7d4a72;
    --varnish: #b9b9bc;
  }
  * { margin: 0; padding: 0; box-sizing: border-box; }
  html, body {
    width: 1200px;
    height: 900px;
    overflow: hidden;
    background: var(--backdrop);
    font-family: "Jost", "Futura", sans-serif;
  }
  .stage {
    position: relative;
    width: 1200px;
    height: 900px;
  }
  .card {
    position: absolute;
    top: 300px;
    width: 520px;
    height: 298px;
    border-radius: 4px;
  }
  .card-front {
    left: 55px;
    background: var(--card-black);
    display: flex;
    flex-direction: column;
    align-items: center;
    justify-content: center;
    gap: 22px;
  }
  .front-mark {
    width: 18px;
    height: 18px;
    border-radius: 50%;
    background: var(--varnish);
  }
  .front-name {
    color: var(--varnish);
    font-size: 24px;
    font-weight: 400;
    letter-spacing: 0.42em;
    text-transform: uppercase;
    padding-left: 0.42em;
  }
  .card-back {
    left: 625px;
    background: var(--card-white);
    color: var(--ink);
  }
  .back-brand {
    position: absolute;
    top: 40px;
    left: 36px;
    display: flex;
    align-items: center;
    gap: 14px;
  }
  .back-mark {
    width: 26px;
    height: 26px;
    border-radius: 50%;
    background: var(--ink);
  }
  .back-name {
    font-size: 22px;
    font-weight: 400;
    letter-spacing: 0.4em;
    text-transform: uppercase;
    color: var(--ink);
  }
  .contact {
    position: absolute;
    left: 36px;
    bottom: 62px;
    font-size: 12px;
    line-height: 1.55;
  }
  .contact-name {
    color: var(--plum);
    font-size: 15px;
    text-transform: uppercase;
    margin-bottom: 8px;
  }
  .contact-label { color: var(--plum); margin-right: 3px; }
  .address {
    position: absolute;
    right: 30px;
    bottom: 30px;
    font-size: 12px;
    line-height: 1.45;
    text-align: left;
  }
  .address-web { color: var(--plum); }
</style>
</head>
<body>
  <main class="stage">
    <section class="card card-front" aria-label="Card front">
      <span class="front-mark"></span>
      <h1 class="front-name">Amber Finch</h1>
    </section>

    <section class="card card-back" aria-label="Card back">
      <div class="back-brand">
        <span class="back-mark"></span>
        <span class="back-name">Amber Finch</span>
      </div>

      <div class="contact">
        <p class="contact-name">Helena Marsh</p>
        <p><span class="contact-label">P</span>01492 718 263</p>
        <p><span class="contact-label">E</span>helena@amberfinchevents.co.uk</p>
      </div>

      <address class="address" style="font-style: normal;">
        <p>Unit 12b Larkfield Barns,</p>
        <p>Upper Hollow, Conwy Vale</p>
        <p>LL28 4QT</p>
        <p class="address-web">www.amberfinchevents.co.uk</p>
      </address>
    </section>
  </main>
</body>
</html>
```